R. K. Dalby, CPA & Associates, LLC
Your Accounting, Finance, and Tax Specialist
R. K. Dalby, CPA & Associates, LLC -
Use specific fonts
open to fonts
Professional
Rennick K. Dalby, CPA
President
4718 Copper Wren Ave. West Palm Beach, FL 33952
rennickdalbycpa@mailnook.test

```html
<!DOCTYPE html>
<html lang="en">
<head>
<meta charset="utf-8">
<title>R. K. Dalby, CPA &amp; Associates, LLC — Business Card</title>
<link href="https://fonts.googleapis.com/css2?family=Cinzel:wght@400&family=Montserrat:wght@400&family=Open+Sans:wght@400;600&display=swap" rel="stylesheet">
<style>
  :root {
    --backdrop: #2b2b2b;
    --card: #ffffff;
    --plum-dark: #8e2a63;
    --plum: #b04a8a;
    --plum-light: #c96aa4;
    --rule-grey: #a3a3a3;
    --text-grey: #6a6a6a;
    --tag-grey: #8a8a8a;
  }
  * { margin: 0; padding: 0; box-sizing: border-box; }
  html, body {
    width: 1200px; height: 959px; overflow: hidden;
    background: var(--backdrop);
  }
  .business-card {
    position: absolute; left: 50px; top: 161px;
    width: 1100px; height: 637px;
    background: var(--card);
    font-family: "Open Sans", Arial, sans-serif;
    color: var(--text-grey);
  }
  .band {
    position: absolute; left: 0; width: 100%;
    background: linear-gradient(90deg, var(--plum-dark), var(--plum-light) 50%, var(--plum-dark));
  }
  .band--top { top: 0; height: 37px; }
  .band--bottom { bottom: 0; height: 40px; }
  .rule {
    position: absolute; left: 0; width: 100%; height: 7px;
    background: linear-gradient(180deg, #c4c4c4, var(--rule-grey));
  }
  .rule--top { top: 41px; }
  .rule--bottom { bottom: 45px; }

  .brand-mark {
    position: absolute; left: 130px; top: 110px;
    width: 160px; height: 160px;
    background: var(--plum);
  }
  .brand-divider {
    position: absolute; left: 364px; top: 78px;
    width: 2px; height: 230px;
    background: #b8b8b8;
  }
  .brand-name {
    position: absolute; left: 392px; top: 122px;
    font-family: "Cinzel", "Times New Roman", serif;
    font-weight: 400;
    color: var(--plum);
    line-height: 1;
  }
  .brand-name__line1 { display: block; font-size: 68px; letter-spacing: 1px; }
  .brand-name__line2 { display: block; font-size: 38px; margin-top: 10px; letter-spacing: 1px; }
  .tagline {
    position: absolute; left: 394px; top: 268px;
    font-family: "Montserrat", Arial, sans-serif;
    font-size: 19px; letter-spacing: 2.5px;
    color: var(--tag-grey);
  }

  .holder {
    position: absolute; left: 0; width: 100%; top: 380px;
    text-align: center; font-size: 29px; font-weight: 600;
  }
  .contact {
    position: absolute; left: 0; width: 100%;
    text-align: center; font-size: 29px;
  }
  .contact--address { top: 492px; }
  .contact--lines { top: 534px; }
  .label { font-weight: 600; }
</style>
</head>
<body>
  <div class="business-card">
    <div class="band band--top"></div>
    <div class="rule rule--top"></div>

    <div class="brand-mark" aria-hidden="true"></div>
    <div class="brand-divider"></div>
    <div class="brand-name">
      <span class="brand-name__line1">R. K. Dalby,</span>
      <span class="brand-name__line2">CPA &amp; Associates, LLC</span>
    </div>
    <p class="tagline">Your Accounting, Finance, and Tax Specialists</p>

    <p class="holder">Rennick K. Dalby, CPA | President</p>
    <p class="contact contact--address"><span class="label">A:</span> 4718 Copper Wren Ave. West Palm Beach, FL 33952</p>
    <p class="contact contact--lines"><span class="label">P:</span> 561.470.2815 | <span class="label">F:</span> 561.470.2816 | <span class="label">E:</span> rennickdalbycpa@mailnook.test</p>

    <div class="rule rule--bottom"></div>
    <div class="band band--bottom"></div>
  </div>
</body>
</html>
```